Psychologist website

Simple psychologist website
Site map:
home
self-test
common conditions
children
contact
about
info

Current website:
http://www.corvalepsychology.com.au/

Not in love with logo, or colours etc - open brief
Happy for new font/style/logo for company name

Customer wants clean, credible and warm and friendly look & feel
stock photos OK

Brief:

One home page - simple with 2 or 3 small areas to tease and attract the user and one template page to suit all the other pages

Pages structurally similar to
http://www.wendlecourt.com.au/
In that the home page is different and the other pages are based on one template

Requirements
Must have
• 2 pages - one home page and one template page
• navigation for site map

```html
<!DOCTYPE html>
<html lang="en">
<head>
<meta charset="utf-8">
<title>Corvale &amp; Associates Clinical Psychologists</title>
<link href="https://fonts.googleapis.com/css2?family=Questrial&family=Arimo:wght@400;700&display=swap" rel="stylesheet">
<style>
  :root {
    --blue: #0aa2cb;
    --green: #6cc21c;
    --grey-text: #6b6b6b;
    --white: #ffffff;
    --footer-soft: #e6f5fa;
    --hero-a: #d9dce0;
    --hero-b: #b9bcc0;
  }
  * { box-sizing: border-box; margin: 0; padding: 0; }
  html, body { width: 958px; height: 1200px; overflow: hidden; background: var(--white); }
  body { position: relative; font-family: "Questrial", sans-serif; color: var(--grey-text); }
  a { text-decoration: none; color: inherit; }

  .site-header { position: absolute; top: 0; left: 0; width: 958px; height: 83px; }
  .brand { position: absolute; left: 24px; top: 14px; display: flex; align-items: center; gap: 10px; }
  .brand-dot { width: 30px; height: 30px; border-radius: 50%; background: var(--green); }
  .brand-name { color: var(--blue); font-size: 23px; line-height: 26px; letter-spacing: 0.2px; }
  .contact-cta { position: absolute; right: 22px; top: 18px; text-align: right; }
  .contact-cta .lead { color: var(--blue); font-size: 14px; }
  .contact-cta .phone { color: var(--green); font-size: 30px; line-height: 38px; }
  .contact-cta .phone strong { font-family: "Arimo", sans-serif; font-weight: 700; }

  .main-nav { position: absolute; top: 83px; left: 0; width: 958px; height: 38px; background: var(--blue); }
  .main-nav ul { list-style: none; display: flex; height: 100%; align-items: center; padding-left: 35px; }
  .main-nav li { color: var(--white); font-size: 19px; margin-right: 49px; }

  .hero { position: absolute; top: 121px; left: 0; width: 958px; height: 470px;
          background: linear-gradient(100deg, var(--hero-a) 0%, #cfd2d4 45%, var(--hero-b) 100%); }
  .hero-caption { position: absolute; left: 23px; top: 281px; width: 364px; height: 126px;
                  background: rgba(10, 162, 203, 0.9); border-radius: 3px;
                  color: var(--white); font-size: 16.5px; line-height: 19.5px; padding: 25px 20px 0 26px; }

  .intro { position: absolute; top: 642px; left: 0; width: 958px; text-align: center; }
  .locations { color: var(--blue); font-size: 22px; letter-spacing: -0.5px; margin-bottom: 30px; padding-left: 40px; }
  .locations span { margin: 0 9px; }
  .intro p { font-size: 14px; line-height: 17px; width: 830px; margin: 0 auto 16px; }
  .intro p a { color: var(--green); }

  .teasers { position: absolute; top: 855px; left: 0; width: 958px; }
  .teaser { position: absolute; top: 0; width: 260px; }
  .teaser-icon { position: absolute; top: 3px; width: 50px; height: 60px; border-radius: 6px; }
  .teaser-body { position: absolute; top: 0; left: 62px; width: 162px; }
  .teaser h2 { color: var(--green); font-weight: 400; font-size: 22px; letter-spacing: -0.6px; line-height: 24px; }
  .teaser p { font-family: "Arimo", sans-serif; font-size: 11.7px; line-height: 14.2px; color: var(--grey-text); }
  .teaser .downloads { list-style: none; margin-top: 4px; }
  .teaser .downloads li { font-family: "Arimo", sans-serif; font-size: 11.7px; line-height: 14px; color: var(--blue); margin-bottom: 7px; }
  .read-more { display: block; margin-top: 6px; font-family: "Arimo", sans-serif; font-weight: 700; font-size: 10.5px; color: var(--blue); }

  .site-footer { position: absolute; top: 1086px; left: 0; width: 958px; height: 114px; background: var(--blue); text-align: center; }
  .footer-nav { margin-top: 34px; font-family: "Arimo", sans-serif; font-size: 12.3px; color: var(--white); }
  .footer-nav a { margin: 0 3px; }
  .copyright { margin-top: 9px; font-family: "Arimo", sans-serif; font-size: 10.5px; color: var(--footer-soft); }
</style>
</head>
<body>
  <header class="site-header">
    <div class="brand">
      <span class="brand-dot"></span>
      <div class="brand-name">CORVALE &amp; ASSOCIATES<br>CLINICAL PSYCHOLOGISTS</div>
    </div>
    <div class="contact-cta">
      <div class="lead">for all appointments and enquiries</div>
      <div class="phone">call <strong>95550142</strong></div>
    </div>
  </header>

  <nav class="main-nav">
    <ul>
      <li>home</li><li>self-test</li><li>common conditions</li><li>children</li><li>about</li><li>info</li><li>contact</li>
    </ul>
  </nav>

  <section class="hero" role="img" aria-label="Photo of a smiling psychologist taking notes with a couple seated on a sofa in a bright office">
    <div class="hero-caption">Psychologists, in Sydney, Chatswood, and Westmead. We provide expert treatment for depression, anxiety, eating disorders and other issues.</div>
  </section>

  <section class="intro">
    <div class="locations"><span>Sydney CBD</span> <span>Chatswood</span> <span>Westmead</span></div>
    <p>Specialising in cognitive-behaviour therapy (CBT) for adults experiencing difficulties with depression, anxiety, eating disorders, stress, trauma, adjustment to illness or disability, and other <a href="#">common issues</a>.</p>
    <p>We also offer therapy and assessment for children and adolescents and their families experiencing problems with anxiety, behaviour, anger, sleep, depression, <a href="#">ADHD</a> and other <a href="#">common issues</a>.</p>
  </section>

  <section class="teasers">
    <article class="teaser" style="left:35px;">
      <div class="teaser-icon" role="img" aria-label="Icon of a doctor with a stethoscope" style="background:linear-gradient(#e4eef2,#b9d3dc);"></div>
      <div class="teaser-body">
        <h2>About Us</h2>
        <p>Our psychologists provide a comfortable, supportive, and confidential environment for their clients. Our first goal is for you to feel comfortable in exploring issues and sharing sharing your concerns, knowing that you have been heard and understood.</p>
        <a class="read-more" href="#">read more +</a>
      </div>
    </article>
    <article class="teaser" style="left:340px;">
      <div class="teaser-icon" role="img" aria-label="Icon of a checklist clipboard with a magnifying glass" style="left:0;width:78px;background:linear-gradient(#e8f0f3,#9fc3d1);"></div>
      <div class="teaser-body" style="left:89px;">
        <h2>Self Test</h2>
        <p>Our psychologists provide a comfortable, supportive, and confidential environment for their clients. Our first goal is for you to feel comfortable in exploring issues and sharing sharing your concerns, knowing that you have been heard and understood.</p>
        <a class="read-more" href="#">read more +</a>
      </div>
    </article>
    <article class="teaser" style="left:690px;">
      <div class="teaser-icon" role="img" aria-label="Icon of a tooth" style="width:42px;height:56px;background:linear-gradient(#f2f7f9,#c3dde6);"></div>
      <div class="teaser-body" style="left:62px;width:172px;">
        <h2>Dental Phobia</h2>
        <p>Handouts from the talk by Dana on managing dental phobia are available here to down load:</p>
        <ul class="downloads">
          <li>Slideshow Presentation</li>
          <li>Dental Phobia Talk/Assessment Checklist.pdf</li>
          <li>Dental Phobia Talk/Hints for patients with phobias.pdf</li>
        </ul>
        <a class="read-more" href="#">read more +</a>
      </div>
    </article>
  </section>

  <footer class="site-footer">
    <nav class="footer-nav">
      <a href="#">Home</a> <a href="#">Self-test</a> <a href="#">Common conditions</a> <a href="#">Children</a> <a href="#">About</a> <a href="#">Info</a> <a href="#">Contact</a>
    </nav>
    <div class="copyright">© Copyright 2013 Northline. All Rights Reserved</div>
  </footer>
</body>
</html>
```